Hollybrook Hounds Jamboree Sponsor & Stallholder Leaflet Design

Hollybrook Hounds Jamboree is the updated and refreshed version of the Pemberly Canine Fete (See www.pemberlycaninefete.co.uk).
Under new management, we need a leaflet designed to promote the event to potential stallholders and sponsors.
Hollybrook Hounds Jamboree is a fun day out for dogs and their human companions, with a range of activities for both.
As this is an outdoor event, we would like this theme in the leaflet.
It is being held in the grounds of Thistlecombe Grange - http://www.thistlecombegrange.com
Note:
Leaflet format of DL/6 page is preferred, but will accept A5/4page
I will require the final work in InDesign format
Target Market(s)
Dog owners and lovers
Industry/Entity Type
Event
Look and feel
Each slider illustrates characteristics of the customer's brand and the style your logo design should communicate.

```html
<!DOCTYPE html>
<html lang="en">
<head>
<meta charset="utf-8">
<title>Hollybrook Hounds Jamboree – Sponsor &amp; Stallholder Leaflet</title>
<link href="https://fonts.googleapis.com/css2?family=Yanone+Kaffeesatz:wght@400;600&family=Questrial&display=swap" rel="stylesheet">
<style>
:root{
  --blue:#1c6fe0;
  --blue-dark:#1558c4;
  --cyan:#2fd3ef;
  --cyan-soft:#8fe6f7;
  --paper-top:#ffffff;
  --paper-bottom:#e6e7e9;
  --fold:#555;
  --white:#fff;
}
*{box-sizing:border-box;margin:0;padding:0}
html,body{width:811px;height:1200px;overflow:hidden;background:#fff}
body{position:relative;font-family:"Questrial",Arial,sans-serif;color:var(--blue);font-size:7.2px;line-height:1.18}
.fold-line{position:absolute;top:40px;bottom:0;width:0;border-left:1px dashed var(--fold)}
.sheet{position:absolute;left:66px;width:684px;height:483px;
  background:linear-gradient(180deg,var(--paper-top) 0%,var(--paper-top) 55%,var(--paper-bottom) 100%);
  box-shadow:0 4px 14px rgba(0,0,0,.18);border:1px solid #d6d6d6}
.sheet--outer{top:68px}
.sheet--inner{top:620px}
.panel{position:absolute;top:0;height:100%;width:228px;padding:8px 10px}
.panel--left{left:0}.panel--mid{left:228px}.panel--right{left:456px}
.heading{font-family:"Yanone Kaffeesatz",Arial Narrow,sans-serif;font-weight:600;line-height:1}
.cyan{color:var(--cyan)}
.photo{position:absolute}
b{font-weight:700}

/* application form */
.form-title{font-size:17px;color:var(--blue)}
.form-sub{font-size:8.5px;font-weight:700;margin-bottom:5px}
table.grid{width:100%;border-collapse:collapse;margin-bottom:4px}
table.grid td,table.grid th{border:1px solid var(--blue);height:10.5px;font-size:5.6px;padding:0 3px;text-align:left}
table.grid th{background:var(--blue);color:var(--white);font-weight:700}
table.details td:first-child{width:52px;color:var(--cyan);font-weight:700}
.form-note{font-size:5.6px;color:var(--cyan);margin:5px 0 3px}
.form-label{font-size:6px;font-weight:700;margin:3px 0 1px}
.tiny{font-size:5px;margin-bottom:6px}

/* cover */
.cover-title{font-size:31px;text-align:center;margin-top:22px}
.cover-date{font-size:24px;text-align:center;margin-top:10px}
.cover-paws{position:absolute;left:176px;top:112px;width:34px;height:30px;border-radius:8px;background:#d2d3d5}
.cover-offer{font-size:23px;text-align:center;color:var(--cyan);margin-top:44px;font-weight:400}

/* inner */
.story{position:absolute;left:0;top:0;width:221px;height:184px;background:var(--blue);color:var(--white);padding:8px 9px 0 9px;font-size:6.9px}
.h2{font-size:17.5px;color:var(--cyan);margin:7px 0 2px;font-weight:400}
.h3{font-size:9.5px;font-weight:700;margin:7px 0 2px;font-family:"Questrial",Arial,sans-serif}
ul.list{list-style:none}
ul.list li::before{content:"• "}
ul.promo{list-style:none;padding-left:24px;font-weight:700}
ul.promo li::before{content:"› ";color:var(--cyan)}
.price-row{display:flex;gap:6px}
.price-row span:first-child{width:48px}
.extra{position:absolute;left:0;right:0;bottom:0;height:226px;background:var(--cyan);color:var(--white);padding:4px 10px}
.extra .h2{color:var(--white);margin-top:0}
.extra .h3{color:var(--blue);margin:3px 0 1px}
.advert td{padding-right:10px;font-size:6.9px}
.advert th{font-size:6.9px;color:var(--blue);text-align:left}
</style>
</head>
<body>

<div class="fold-line" style="left:294px"></div>
<div class="fold-line" style="left:523px"></div>

<!-- OUTER SHEET -->
<section class="sheet sheet--outer">
  <div class="panel panel--left">
    <div class="heading form-title">Hollybrook Hounds Jamboree 2013</div>
    <div class="form-sub">Exhibitor Space Application Form</div>
    <table class="grid details">
      <tr><td>Business Name</td><td></td></tr>
      <tr><td>Business Address</td><td></td></tr>
      <tr><td></td><td></td></tr><tr><td></td><td></td></tr>
      <tr><td>Postcode</td><td></td></tr>
      <tr><td>Business Website</td><td></td></tr>
      <tr><td>Contact Name</td><td></td></tr>
      <tr><td>Contact Email</td><td></td></tr>
      <tr><td></td><td></td></tr>
    </table>
    <div class="form-note">Space Required<br>Note - All Prices Exclude VAT</div>
    <div class="form-label">Outside</div>
    <table class="grid">
      <tr><th>Space</th><th>Price</th><th></th><th>Total</th></tr>
      <tr><td>3m(w) x 6m(d)</td><td>@ £150</td><td></td><td></td></tr>
      <tr><td>6m(w) x 10m(d)</td><td>@ £250</td><td></td><td></td></tr>
      <tr><td>9m(w) x 10m(d)</td><td>@ £350</td><td></td><td></td></tr>
      <tr><td>12m(w) x 10m(d)</td><td>@ £450</td><td></td><td></td></tr>
    </table>
    <div class="form-label">Inside</div>
    <table class="grid">
      <tr><th>Space</th><th>Price</th><th>Quantity</th><th>Total</th></tr>
      <tr><td>Marquee Space<br>Minimum 6m2</td><td>@ £15/m2</td><td></td><td></td></tr>
      <tr><td>Power<br>Per 13amp Socket</td><td>@ £30each</td><td></td><td></td></tr>
      <tr><td>Table (6' x 2'6")</td><td>@ £10each</td><td></td><td></td></tr>
    </table>
    <div class="form-label">Show Guide Advert</div>
    <table class="grid">
      <tr><th>Space - mm's</th><th>Price</th><th>Quantity</th><th>Total</th></tr>
      <tr><td>Back cover - 148w x 210h</td><td>£350</td><td></td><td></td></tr>
      <tr><td>Full page - 148w x 210h</td><td>£250</td><td></td><td></td></tr>
      <tr><td>Half Page - 148w x 105h</td><td>£135</td><td></td><td></td></tr>
      <tr><td>Quarter Page - 74w x 105h</td><td>£75</td><td></td><td></td></tr>
      <tr><td>Sixth Page - 74w x 70h</td><td>£50</td><td></td><td></td></tr>
      <tr><td>Voucher Booklet</td><td>£50</td><td></td><td></td></tr>
      <tr><td>Banners (60cm high)</td><td>@ £10 per mtr</td><td></td><td></td></tr>
    </table>
    <div class="tiny">In Competition Rings - design &amp; print not included</div>
    <table class="grid">
      <tr><td style="color:var(--cyan)">Sub Total</td><td></td></tr>
      <tr><td style="color:var(--cyan)">VAT @ 20%</td><td></td></tr>
      <tr><td style="color:var(--cyan)">Grand Total</td><td></td></tr>
      <tr><td style="color:var(--cyan)">Deposit</td><td style="text-align:right">£50</td></tr>
      <tr><td style="color:var(--cyan)">Outstanding</td><td></td></tr>
    </table>
  </div>

  <div class="panel panel--mid" style="padding-top:38px;font-size:7.6px">
    <p>To secure the booking this form must be fully completed and signed AND accompanied by the deposit and a post dated cheque (made payable to Marlowe Events Ltd) for the outstanding balance dated one month prior to the show.<br>If you are paying by debit/credit card, we will call you to take the deposit payment.<br>Bookings are subject to terms &amp; conditions and booking the event confirms that you accept these conditions.</p>
    <p class="cyan" style="font-weight:700;margin-top:12px">PLEASE RETURN COMPLETED FORM TO - Hollybrook Hounds Jamboree, Marlowe Events Ltd, 7 Alderbank Lane, Little Wrenham, Fernley FN12 4QD</p>
    <div class="photo" role="img" aria-label="Photo of a dog lying on green grass" style="left:0;top:225px;width:155px;height:100px;border-radius:0 12px 12px 0;background:linear-gradient(160deg,#5e9a3a 0%,#7fbf45 45%,#b6d66a 70%,#4f8a2c 100%)"></div>
    <div style="position:absolute;left:10px;right:6px;top:382px;text-align:center">
      <p style="font-size:10px;font-weight:700;font-style:italic">To book or for more information contact the Hollybrook Hounds team:</p>
      <p style="font-size:8px;margin-top:5px">Call - <b style="font-size:12px">01632 960418</b></p>
      <p style="font-size:7.6px;margin-top:4px">email - <b>contact@hollybrookhounds.co.uk</b></p>
      <p style="font-size:7.6px;margin-top:3px">website - <b style="font-size:10px">www.hollybrookhounds.co.uk</b></p>
      <p class="cyan" style="margin-top:10px;font-size:7.4px">This event is organised &amp; managed by<br><b>Marlowe Events Ltd</b><br>7 Alderbank Lane, Little Wrenham, Fernley<br>FN12 4QD</p>
    </div>
  </div>

  <div class="panel panel--right" style="padding:0 6px">
    <div class="heading cover-title" style="font-size:29px">Hollybrook Hounds Jamboree</div>
    <div class="heading cover-date" style="font-weight:400">27th &amp; 28th July 2013</div>
    <div class="cover-paws" role="img" aria-label="Decorative paw prints"></div>
    <div class="heading cover-offer">Sponsorship &amp; Trade<br>Exhibitor Opportunities</div>
    <div class="photo" role="img" aria-label="Photo of a dog leaning out of a blue car window under a sunny sky" style="left:10px;top:222px;width:218px;height:261px;border-radius:10px 0 0 0;background:linear-gradient(180deg,#cfe9fb 0%,#6fb3ea 30%,#3f86d6 62%,#5a9a3c 80%,#8bbf55 100%)"></div>
  </div>
</section>

<!-- INNER SHEET -->
<section class="sheet sheet--inner">
  <div class="panel panel--left" style="padding-top:196px">
    <div class="story">
      <b>Pemberly Canine Fete</b> was created and launched in 2009, in aid of Forces Kin Trust, co-inciding with the deployment of the Wessex Lancers on active service to Afghanistan. Parents left behind during their deployment where amongst the committed volunteers who participated and helped in the organisation of the event. The event captured the animal loving spirit of Wrenshire at a point when the whole county was passionate in their support of 'our blokes doing their bit' in Afghanistan. Expecting a few hundred dogs and 5,000 humans, it actual attracted circa 1,000 dogs, with almost 15,000 guests, the inaugural event was seen as an outstanding success. 2010 saw a visitor increase of circa 20%.<br>Due to the overwhelming footfall, 2013 will become a two day event and is now known as 'Hollybrook Hounds Jamboree'.
    </div>
    <div class="heading h2">Where Is It Held?</div>
    <p>Thistlecombe Grange is one of Wrenshire's most romantic and impressive large Edwardian country houses set in sweeping parkland. It was built to a grand design by Edmund Arthur Vale, grandson of Edmund Vale, the inventor of modern holiday travel, and is lived in today by his descendants. Although a private family home, and not open to the public, Thistlecombe Grange offers a unique and magical venue for the Hollybrook Hounds Jamboree.<br>Near Ashcombe, in North Wrenshire, Thistlecombe Grange is approximately 30 minutes from Kingsmere.</p>
    <div class="heading h2">Who Will Attend?</div>
    <p>The target audience for this event is anyone who likes, owns or has an interest in dogs!<br>Heavily promoted to dog lovers and owners, across several mediums, it attracts visitors of all ages across the demographic spectrum.</p>
    <div class="heading h2">How Will It Be Promoted</div>
    <ul class="promo">
      <li>Dedicated website</li>
      <li>Social Media - Friendloop, Chirpline etc</li>
      <li>Regional Advertising</li>
      <li>Dog &amp; pet Press</li>
      <li>Regional Radio</li>
      <li>Regional database via email</li>
    </ul>
  </div>

  <div class="panel panel--mid">
    <div class="heading h2" style="margin-top:0;font-size:19px">Sponsorship</div>
    <div class="h3" style="margin-top:1px">Why sponsor</div>
    <ul class="list">
      <li>Give your brands or products exposure to circa 20,000 visitors</li>
      <li>Access a highly targeted market</li>
      <li>Lead generation</li><li>Brand positioning</li><li>Increase brand recognition</li>
    </ul>
    <div class="h3">What Does Sponsorship Give You?</div>
    <p>There are four types of sponsorship, dependant of your budget and marketing goals.</p>
    <div class="h3">Main Event Sponsor</div>
    <ul class="list">
      <li>Branding on all media communications - leaflets, tickets, website, emails etc</li>
      <li>Large Exhibition Space</li>
      <li>Sign and Banner Rights across the event venue and rings (banner production included)</li>
      <li>Local, regional and national Media Exposure</li>
      <li>2 pages in the show guide</li>
      <li>Global Judging rights</li>
      <li>Massive Consumer Awareness</li>
      <li>20 Complimentary tickets</li>
    </ul>
    <div class="h3">Ring Sponsor</div>
    <ul class="list">
      <li>Exhibition Space</li>
      <li>Joint Banner Rights in the event ring (banner production included)</li>
      <li>1 pages in the show guide</li><li>Ring Judging rights</li><li>5 Complimentary tickets</li>
    </ul>
    <div class="h3">Competition Sponsor</div>
    <ul class="list">
      <li>Exhibition Space</li><li>1/2 page in the show guide</li><li>Competition Judging rights</li><li>2 Complimentary tickets</li>
    </ul>
    <div class="h3">Gift/Sample Sponsor</div>
    <ul class="list">
      <li>Promote your brand or product by supplying gift or sample</li>
      <li>Data collection opportunity</li><li>Exhibition Space</li><li>1/2 page in the show guide</li>
    </ul>
    <div class="photo" role="img" aria-label="Illustration of a running dog" style="left:148px;top:418px;width:70px;height:52px;border-radius:6px;background:linear-gradient(135deg,#2a3340,#5a6470)"></div>
  </div>

  <div class="panel panel--right">
    <div class="heading h2" style="margin-top:0;font-size:19px">Trade Exhibitors</div>
    <p>There are several space options available to exhibitors, both covered and grass space only.<br>Covering the two days of the event, exhibitors also get a line listing in the event show guide and website.</p>
    <div role="img" aria-label="Decorative paw prints" style="position:absolute;left:172px;top:70px;width:50px;height:26px;border-radius:8px;background:#d2d3d5"></div>
    <div class="h3" style="margin-top:12px">Grass Space only</div>
    <div class="price-row"><span>3m(w) x 6m(d)</span><span>£150</span></div>
    <div class="price-row"><span>6m(w) x 10m(d)</span><span>£250</span></div>
    <div class="price-row"><span>9m(w) x 10m(d)</span><span>£350</span></div>
    <div class="price-row"><span>12m(w) x 10m(d)</span><span>£450</span></div>
    <p style="margin-top:8px"><b style="font-size:9.5px">Marquee Space</b> - £15 per square meter (minimum 6 square meters)</p>
    <p style="margin-top:8px"><b style="font-size:9.5px">Power (Marquee Only)</b> - £30 per 13amp Socket</p>
    <p style="margin-top:8px"><b style="font-size:9.5px">Table (6' x 2'6")</b> &nbsp;&nbsp;&nbsp;&nbsp;&nbsp;&nbsp;&nbsp;&nbsp; - £10 each</p>
    <p style="margin-top:8px"><b>Notes:</b><br>• All exhibitors must have valid and suitable public, product &amp; employee liability insurance<br>• All (human) food based exhibitors must have suitable food hygiene qualifications and certification</p>

    <div class="extra">
      <div class="heading h2" style="font-size:19px">Additional Marketing Opportunities</div>
      <div class="h3">Show Guide</div>
      <p>A minimum of 32 pages, the show guide not only contains useful features and stories, but also a full listing of all sponsors and exhibitors.</p>
      <table class="advert" style="border-collapse:collapse;margin-top:2px">
        <tr><th></th><th>Exhibitor</th><th>Standard Advertiser</th></tr>
        <tr><td>Back cover</td><td>£350</td><td>£700</td></tr>
        <tr><td>Full page</td><td>£250</td><td>£500</td></tr>
        <tr><td>Half Page</td><td>£135</td><td>£2700</td></tr>
        <tr><td>Quarter Page</td><td>£75</td><td>£150</td></tr>
        <tr><td>Sixth Page</td><td>£50</td><td>£100</td></tr>
      </table>
      <div class="h3">Promotional Voucher</div>
      <p>The centre of the guide will contain a pull out voucher booklet, with 6 vouchers per page.<br>Exhibitors offering a special promotion, price or service during the event can promote it via a voucher, which will not only highlight the offer, but also identify the location of their stand.<br>This costs £50 per voucher.</p>
      <p style="margin-top:3px"><b style="color:var(--blue);font-size:9px">Banners In Competition Rings</b> - £10 per meter (60cm high) - design &amp; production not included</p>
    </div>
  </div>
</section>

</body>
</html>
```